Brightpath Orthodontics appointment card design

I need appointment cards/ business cards made. Front will be Logo, name, title, email, phone number and location (5274 Willowmere Pkwy, Ste 312, Concord, NC 28027) . the back should have an appointment card (name, time, date) and also 3 addresses listed with a check box so we can check to which location they are going.
Brent Pellman Orthodontics
- 6315 Harlow Avenue, Ste 104, Harrisburg, NC 28075
- 2947 Rosvale Court SW, Ste 500, Concord, NC 28025
- 7163 Fernbrook Corporate Parkway, Ste 404, Charlotte, NC 28277
Business card can be horizontal or vertical in Design.
I need to be able to edit it to update and add new employees

Requirements
Must have
• Front:
• - Logo
• - Name & Title (able to be edited)
• - phone (704-555-0148) & Email (need to be able to edit)
• - Address: 5274 Willowmere Pkwy, Ste 312
• Concord, NC 28027
• Back:
• Appointment Card design:
• - Name, time, Date
• - 3 locations w/ a check box so the patient knows where to go:
• Brent Pellman Orthodontics
• - 6315 Harlow Avenue, Ste 104, Harrisburg, NC 28075
• - 2947 Rosvale Court SW, Ste 500, Concord, NC 28025
• - 7163 Fernbrook Corporate Parkway, Ste 404, Charlotte, NC 28277

```html
<!DOCTYPE html>
<html lang="en">
<head>
<meta charset="utf-8">
<title>Brightpath Orthodontics – Business &amp; Appointment Card</title>
<link href="https://fonts.googleapis.com/css2?family=Poppins:wght@400;500;600;700&display=swap" rel="stylesheet">
<style>
  :root {
    --page: #e6eaef;
    --card: #ffffff;
    --blue: #1a7cc4;
    --blue-light: #2a91d6;
    --blue-dark: #0b4f94;
    --ink-blue: #1565b0;
    --grey: #6f7680;
    --line: #4a4f57;
    --faint: #e9f1f8;
  }
  * { margin: 0; padding: 0; box-sizing: border-box; }
  html, body { width: 1200px; height: 900px; overflow: hidden; }
  body {
    background: var(--page);
    font-family: "Poppins", sans-serif;
    position: relative;
  }
  .card {
    position: absolute;
    left: 250px;
    width: 700px;
    height: 400px;
    background: var(--card);
    border-radius: 34px;
    overflow: hidden;
    box-shadow: 0 10px 30px rgba(20, 40, 70, 0.18);
  }
  .card--front { top: 35px; }
  .card--back { top: 465px; }
  .card__wave { position: absolute; inset: 0; width: 100%; height: 100%; }
  .abs { position: absolute; }

  /* Front */
  .person__name {
    left: 44px; top: 34px;
    font-size: 25px; font-weight: 700; color: var(--ink-blue);
    letter-spacing: 0.5px;
  }
  .person__title {
    left: 44px; top: 68px;
    font-size: 12px; color: var(--grey); letter-spacing: 1px;
  }
  .contact {
    left: 40px; top: 160px;
    list-style: none;
    color: #ffffff; font-size: 17px;
  }
  .contact li { display: flex; align-items: center; gap: 12px; margin-bottom: 8px; }
  .contact svg { width: 16px; height: 16px; flex: none; }
  .brand {
    right: 40px; top: 120px;
    display: flex; align-items: center; gap: 12px;
  }
  .brand__dot {
    width: 26px; height: 26px; border-radius: 50%;
    background: var(--ink-blue);
  }
  .brand__name {
    font-size: 30px; font-weight: 600; color: var(--ink-blue);
    line-height: 1.1;
  }
  .office-address {
    right: 44px; bottom: 34px;
    text-align: right; color: #ffffff; font-size: 17px; line-height: 1.45;
  }

  /* Back */
  .brand-watermark {
    left: 150px; top: 60px;
    font-size: 130px; font-weight: 600; color: var(--faint);
    line-height: 1;
  }
  .appt-field {
    display: flex; align-items: flex-end; gap: 12px;
    font-size: 16px; color: var(--ink-blue);
  }
  .appt-field__line { flex: 1; border-bottom: 1.5px solid var(--line); height: 1px; margin-bottom: 5px; }
  .appt-field--name { left: 40px; top: 30px; width: 620px; }
  .appt-field--time { left: 40px; top: 78px; width: 620px; }
  .appt-field--date { left: 380px; top: 150px; width: 280px; }
  .practice-name {
    right: 40px; top: 206px;
    font-size: 19px; font-weight: 700; color: var(--ink-blue);
    letter-spacing: 0.3px;
  }
  .checkbox {
    width: 36px; height: 36px; border-radius: 50%;
    background: #ffffff;
    border: 4px solid var(--blue-dark);
    box-shadow: 0 2px 5px rgba(0, 0, 0, 0.25);
    transform: translate(-50%, -50%);
  }
  .location {
    color: #ffffff; font-size: 13.5px; line-height: 1.35;
  }
  .location--harrisburg { left: 40px; top: 170px; }
  .location--charlotte { left: 230px; top: 260px; }
  .location--concord { left: 480px; top: 318px; }
</style>
</head>
<body>

<section class="card card--front" aria-label="Business card front">
  <svg class="card__wave" viewBox="0 0 700 400" preserveAspectRatio="none" aria-hidden="true">
    <defs>
      <linearGradient id="frontBlue" x1="0" y1="0" x2="1" y2="1">
        <stop offset="0" stop-color="var(--blue-light)"/>
        <stop offset="1" stop-color="var(--blue)"/>
      </linearGradient>
    </defs>
    <path d="M0,90 C200,72 300,190 420,240 C520,282 610,282 700,272 L700,400 L0,400 Z" fill="var(--blue-dark)"/>
    <path d="M0,108 C200,92 300,208 420,256 C520,296 610,296 700,288 L700,400 L0,400 Z" fill="url(#frontBlue)"/>
  </svg>

  <div class="abs person__name">JOHANTHAN DOE</div>
  <div class="abs person__title">TITLE</div>

  <ul class="abs contact">
    <li>
      <svg viewBox="0 0 24 24"><path fill="#fff" d="M6.6 10.8a15.1 15.1 0 0 0 6.6 6.6l2.2-2.2a1 1 0 0 1 1-.25 11.4 11.4 0 0 0 3.6.57 1 1 0 0 1 1 1V20a1 1 0 0 1-1 1A17 17 0 0 1 3 4a1 1 0 0 1 1-1h3.5a1 1 0 0 1 1 1c0 1.25.2 2.45.57 3.57a1 1 0 0 1-.25 1z"/></svg>
      704-555-0148
    </li>
    <li>
      <svg viewBox="0 0 24 24"><path fill="#fff" d="M3 5h18a1 1 0 0 1 1 1v12a1 1 0 0 1-1 1H3a1 1 0 0 1-1-1V6a1 1 0 0 1 1-1zm9 7.2L20 7H4z"/></svg>
      emailaddress@domain.com
    </li>
    <li>
      <svg viewBox="0 0 24 24"><circle cx="12" cy="12" r="9" fill="none" stroke="#fff" stroke-width="2"/><path d="M3 12h18M12 3c3 3 3 15 0 18M12 3c-3 3-3 15 0 18" fill="none" stroke="#fff" stroke-width="1.6"/></svg>
      BrightpathOrthodontics.com
    </li>
  </ul>

  <div class="abs brand">
    <span class="brand__dot"></span>
    <span class="brand__name">Brightpath<br>Orthodontics</span>
  </div>

  <address class="abs office-address" style="font-style:normal">
    5274 Willowmere Pkwy<br>Ste 312, Concord, NC 28027
  </address>
</section>

<section class="card card--back" aria-label="Appointment card back">
  <div class="abs brand-watermark" aria-hidden="true">Brightpath</div>

  <svg class="card__wave" viewBox="0 0 700 400" preserveAspectRatio="none" aria-hidden="true">
    <defs>
      <linearGradient id="backBlue" x1="0" y1="0" x2="1" y2="1">
        <stop offset="0" stop-color="var(--blue-light)"/>
        <stop offset="1" stop-color="var(--blue)"/>
      </linearGradient>
    </defs>
    <path d="M0,108 C170,98 240,200 370,232 C490,262 600,270 700,272 L700,400 L0,400 Z" fill="var(--blue-dark)"/>
    <path d="M0,124 C170,114 240,216 370,248 C490,278 600,286 700,288 L700,400 L0,400 Z" fill="url(#backBlue)"/>
  </svg>

  <div class="abs appt-field appt-field--name"><span>Name</span><span class="appt-field__line"></span></div>
  <div class="abs appt-field appt-field--time"><span>Time</span><span class="appt-field__line"></span></div>
  <div class="abs appt-field appt-field--date"><span>Date</span><span class="appt-field__line"></span></div>

  <div class="abs practice-name">BRENT PELLMAN ORTHODONTICS</div>

  <span class="abs checkbox" style="left:90px; top:120px"></span>
  <span class="abs checkbox" style="left:290px; top:214px"></span>
  <span class="abs checkbox" style="left:540px; top:270px"></span>

  <div class="abs location location--harrisburg">6315 Harlow Avenue<br>Ste 104 Harrisburg<br>NC 28075</div>
  <div class="abs location location--charlotte">7163 Fernbrook<br>Corporate Parkway,<br>Ste 404 Charlotte<br>NC 28277</div>
  <div class="abs location location--concord">2947 Rosvale Court SW<br>Ste 500, Concord<br>NC 28025</div>
</section>

</body>
</html>
```